College Social website needs a SIMPLE chart design

We need a simple one page website. The website is called "Fim-Bosk" a phonetic spelling of the word collage. The site allows users to gain up to date information on the nightlife and social scene of the campus. The site must be able to easily convey several key pieces of information; some type of grid/chart would work well.

This includes:
primary information:
-The name of the bar (about 9 bars on campus)
-The length of the line
-Guy/Girl ratio
-If there is cover (admittance fee) to enter the bar

secondary information:
-how packed/full the bar is
-if there is police raiding the bar
-a way to show more information including drink specials

would prefer a design similar to this page except more colorful/playful/fun: http://m.vantorelq.com/results.php

Some stylistic tips - the name of the service is called fim bosk. a phonetic spelling of collage (http://en.quorbinet.org/wiki/Collage). it doesnt need to look like a rainbow, just be exciting, engaging, and vivid.

look at this page for reference: http://www.plimvadee.com/blog/flat-ui-design-showcase/

other than the bar name and drink specials, everything should be presented graphically. All the bar stats are approximations and rough estimates, so you must find a way to present the information as relatives. historical information is not relevant. only the real time stats need to be included. here is a sample:

Bar name: Sample bar
guy/girl ratio: 70/30
line length: short
admittance fee: yes
bar attendance: near full
police raid: no
drink specials:
WINE NIGHT!
$8 BOTTLES OF GALLOWMERE WINE
$8 BOTTLES OF CHAMPAGNE
$2 TRESK PALE BOTTLES
$2 WELLS

Target Market(s)

target market for the site is 18-21 year olds in college.

Industry/Entity Type

College

Requirements
Must have
• the design MUST be mobile friendly. keep it simple. a flat design would be preferred.
the information must be conveyed in the form of symbols/icons. for instance, a pie chart to show guy/girl ratio.

```html
<!DOCTYPE html>
<html lang="en">
<head>
<meta charset="utf-8">
<title>Fim-Bosk – Find bars near you</title>
<link href="https://fonts.googleapis.com/css2?family=Source+Sans+3:wght@400;600;700&display=swap" rel="stylesheet">
<style>
  :root{
    --page:#f2f2f2;
    --panel:#ffffff;
    --frame:#cfcfcf;
    --brand:#2a9fd0;
    --sky:#4dbde0;
    --sky-soft:#9fdcef;
    --ink:#555555;
    --muted:#8a8a8a;
    --faint:#bdbdbd;
    --coral:#f47252;
    --cyan:#4fcbe6;
    --lime:#a7d33a;
    --track:#e6e6e6;
    --teal-deep:#14a8cc;
    --mint:#2ec4a5;
    --mint-deep:#1b8f78;
    --net-a:#4fb8e8;
    --net-b:#3f5b99;
    --net-c:#ea5c92;
  }
  *{box-sizing:border-box;margin:0;padding:0}
  html,body{width:1200px;height:2249px;overflow:hidden}
  body{position:relative;background:var(--page);font-family:"Source Sans 3",sans-serif;color:var(--ink)}
  .abs{position:absolute}

  .brand{left:86px;top:30px}
  .brand-name{font-size:54px;font-weight:700;color:var(--brand);line-height:1;letter-spacing:-1px}
  .brand-tag{font-size:21px;font-weight:600;color:var(--brand);line-height:1;margin-top:-2px}
  .net-dot{width:42px;height:42px;border-radius:50%;top:55px}

  .panel{left:86px;top:123px;width:1026px;height:2038px;background:var(--panel);border:1px solid var(--frame)}

  .nav-item{top:144px;height:39px;line-height:39px;font-size:23px;font-weight:600;color:#8c8c8c;padding:0 24px}
  .nav-item.is-current{background:#e4f3f9;color:#7d8c93}

  .hero{left:87px;top:199px;width:1024px;height:548px;
    background:radial-gradient(ellipse at 45% 20%,#e2c49a 0%,#9c7a55 30%,#3b2e25 65%,#0c0d14 100%)}
  .finder{left:244px;top:401px;width:761px;height:184px;background:var(--sky)}
  .finder-title{left:302px;top:416px;font-size:55px;font-weight:700;color:#fff;letter-spacing:0.5px}
  .finder-input{left:300px;top:490px;width:492px;height:63px;background:#fff;border:2px solid #3aa8ce;
    font-size:23px;font-weight:600;color:#a9a9a9;line-height:59px;padding-left:30px}
  .finder-go{left:815px;top:490px;width:137px;height:63px;background:var(--sky-soft);
    font-size:40px;font-weight:700;color:#3fb2da;text-align:center;line-height:63px}

  .venue-title{left:125px;top:780px;font-size:46px;font-weight:600;color:var(--brand)}

  .card{background:#fff;border:2px solid #dcdcdc}
  .card-title{position:absolute;left:0;right:0;text-align:center;font-size:21px;color:#6a6a6a}

  .venue-card{left:125px;top:859px;width:277px;height:515px}
  .venue-map{position:absolute;left:0;top:0;width:273px;height:237px;
    background:linear-gradient(135deg,#eceae3 0%,#e4e6d8 40%,#c9d6e4 70%,#e9e7df 100%)}
  .map-tool{position:absolute;left:225px;width:38px;background:var(--sky);color:#fff;text-align:center;font-size:24px;line-height:34px}
  .venue-name{position:absolute;left:32px;top:260px;font-size:18px;color:#666}
  .venue-area{position:absolute;left:32px;top:285px;font-size:13px;color:#a0a0a0}
  .venue-rule{position:absolute;left:0;right:0;top:314px;border-top:1px solid #e2e2e2}
  .reach-row{position:absolute;left:0;width:273px;height:58px}
  .reach-mark{position:absolute;left:0;top:0;width:62px;height:58px}
  .reach-count{position:absolute;left:80px;top:6px;font-size:23px;color:#777}
  .reach-unit{position:absolute;left:80px;top:35px;font-size:10px;color:#b2b2b2}
  .reach-line{position:absolute;left:80px;right:70px;bottom:0;border-top:1px solid #ececec}

  .ratio-card{left:539px;top:859px;width:534px;height:366px}
  .ratio-chart{position:absolute;left:59px;top:68px}
  .legend{position:absolute;left:381px;font-size:18px;color:#999;display:flex;align-items:center;gap:14px}
  .legend i{display:block;width:22px;height:22px}

  .line-card{left:539px;top:1254px;width:534px;height:203px}
  .meter-label{position:absolute;left:95px;font-size:17px;color:#888}
  .meter{position:absolute;left:95px;width:299px;height:13px;background:var(--track)}
  .meter b{display:block;height:100%;background:linear-gradient(90deg,var(--cyan),var(--lime))}
  .meter-value{position:absolute;left:410px;font-size:15px;color:#aaa}

  .fee-card{left:125px;top:1492px;width:467px;height:260px}
  .crowd-card{left:719px;top:1492px;width:354px;height:260px;background:var(--teal-deep)}

  .section-title{left:139px;top:1800px;font-size:35px;font-weight:400;color:var(--ink)}
  .section-rule{left:128px;top:1850px;width:938px;border-top:2px solid #e6e6e6}
  .info-title{font-size:26px;color:#666}
  .info-divider{left:558px;top:1871px;height:273px;border-left:2px solid #e3e3e3}
  .select{width:276px;height:45px;background:#fff;border:2px solid #e0e0e0;box-shadow:0 1px 3px rgba(0,0,0,.08);
    font-size:18px;color:#c2c2c2;line-height:41px;padding-left:14px}
  .select::after{content:"";position:absolute;right:38px;top:6px;height:29px;border-left:1px solid #e2e2e2}
  .select-caret{position:absolute;right:12px;top:8px}

  .footer{left:0;top:2190px;width:1200px;text-align:center;font-size:17px;color:#555}
  .footer span{color:var(--brand)}
</style>
</head>
<body>

<header>
  <div class="abs brand">
    <div class="brand-name">Fim-Bosk</div>
    <div class="brand-tag">Find bars near you</div>
  </div>
  <span class="abs net-dot" style="left:921px;background:var(--net-a)" aria-label="Social network"></span>
  <span class="abs net-dot" style="left:982px;background:var(--net-b)" aria-label="Social network"></span>
  <span class="abs net-dot" style="left:1045px;background:var(--net-c)" aria-label="Social network"></span>
</header>

<main class="abs panel"></main>

<nav>
  <span class="abs nav-item is-current" style="left:98px">Home</span>
  <span class="abs nav-item" style="left:215px">Blog</span>
  <span class="abs nav-item" style="left:317px">Contact us</span>
  <span class="abs nav-item" style="left:482px">About us</span>
</nav>

<section>
  <div class="abs hero" role="img" aria-label="Crowd with raised hands at a concert under warm stage lights"></div>
  <div class="abs finder"></div>
  <div class="abs finder-title">FIND A BAR</div>
  <div class="abs finder-input">TYPE A BAR NEAR YOU</div>
  <div class="abs finder-go">GO</div>
</section>

<h1 class="abs venue-title">Marlow Night Club :</h1>

<!-- Venue card -->
<div class="abs card venue-card">
  <div class="venue-map" role="img" aria-label="Street map around the club"></div>
  <svg class="abs" style="left:55px;top:65px" width="30" height="42" viewBox="0 0 30 42">
    <path d="M15 0C7 0 1 6 1 14c0 10 14 26 14 26s14-16 14-26C29 6 23 0 15 0z" fill="#2aa8d8"/>
    <circle cx="15" cy="14" r="6" fill="#fff"/>
  </svg>
  <div class="map-tool" style="top:175px">+</div>
  <div class="map-tool" style="top:209px;background:#6fcbe6">–</div>
  <div class="map-tool" style="top:243px;height:34px">
    <svg width="14" height="20" viewBox="0 0 30 42" style="margin-top:7px"><path d="M15 0C7 0 1 6 1 14c0 10 14 26 14 26s14-16 14-26C29 6 23 0 15 0z" fill="#fff"/><circle cx="15" cy="14" r="6" fill="#4dbde0"/></svg>
  </div>
  <div class="venue-name">MARLOW CLUB</div>
  <div class="venue-area">State, District</div>
  <div class="venue-rule"></div>

  <div class="reach-row" style="top:341px">
    <span class="reach-mark" style="background:#56c3ea"></span>
    <span class="reach-count">1524</span><span class="reach-unit">Followers</span><span class="reach-line"></span>
  </div>
  <div class="reach-row" style="top:399px">
    <span class="reach-mark" style="background:#4a5e9e"></span>
    <span class="reach-count">20K</span><span class="reach-unit">Likes</span><span class="reach-line"></span>
  </div>
  <div class="reach-row" style="top:457px">
    <span class="reach-mark" style="background:#ee5d93"></span>
    <span class="reach-count">3000</span><span class="reach-unit">Followers</span>
  </div>
</div>

<!-- Guy / girl ratio -->
<div class="abs card ratio-card">
  <div class="card-title" style="top:24px">GUY/GIRL RATIO</div>
  <svg class="ratio-chart" width="276" height="276" viewBox="-138 -138 276 276" font-family="Source Sans 3, sans-serif">
    <circle r="112" fill="none" stroke="var(--coral)" stroke-width="22" stroke-dasharray="391 1000" transform="rotate(70)"/>
    <circle r="110" fill="none" stroke="var(--cyan)" stroke-width="16" stroke-dasharray="165 1000" transform="rotate(-15)"/>
    <circle r="78" fill="#5a5a5a"/>
    <text y="14" text-anchor="middle" font-size="42" fill="#fff">Ratio</text>
    <text x="38" y="112" text-anchor="middle" font-size="11" fill="#fff" transform="rotate(-20 38 112)">60%</text>
    <text x="106" y="46" text-anchor="middle" font-size="11" fill="#fff" transform="rotate(-66 106 46)">25%</text>
  </svg>
  <div class="legend" style="top:97px"><i style="background:var(--coral)"></i>Girls</div>
  <div class="legend" style="top:141px"><i style="background:var(--cyan)"></i>Guys</div>
</div>

<!-- Line length -->
<div class="abs card line-card">
  <div class="card-title" style="top:12px">THE LENGTH OF THE LINE</div>
  <div class="meter-label" style="top:56px">Weekdays</div>
  <div class="meter" style="top:93px"><b style="width:60%"></b></div>
  <div class="meter-value" style="top:88px">60%</div>
  <div class="meter-label" style="top:135px">Weekends</div>
  <div class="meter" style="top:171px"><b style="width:85%"></b></div>
  <div class="meter-value" style="top:166px">80%</div>
</div>

<!-- Admittance fee -->
<div class="abs card fee-card">
  <svg width="463" height="256" viewBox="0 0 266 148" font-family="Source Sans 3, sans-serif">
    <text x="133" y="32" text-anchor="middle" font-size="12" fill="#6a6a6a">ADMITTANCE FEE</text>
    <polygon points="13,127 29,94 45,127" fill="#e8192c"/>
    <polygon points="35,127 58,87 81,127" fill="#b8a078"/>
    <polygon points="57,127 82,87 107,127" fill="#137d8f"/>
    <polygon points="93,127 119,83 145,127" fill="#f39b25"/>
    <polygon points="121,127 148,73 175,127" fill="#ec0f6c"/>
    <polygon points="153,127 186,64 219,127" fill="#fdd23e"/>
    <polygon points="191,127 222,73 253,127" fill="#8d8d8d"/>
    <g font-size="7" fill="#444" text-anchor="middle">
      <text x="31" y="82">$5</text><text x="57" y="78">$5</text><text x="81" y="74">$5</text>
      <text x="118" y="73">$5</text><text x="151" y="68">$10</text><text x="186" y="60">$15</text><text x="222" y="68">$10</text>
    </g>
    <g font-size="5" fill="#999" text-anchor="middle">
      <text x="22" y="139">Monday</text><text x="52" y="139">Tuesday</text><text x="86" y="139">Wednesday</text>
      <text x="122" y="139">Thursday</text><text x="151" y="139">Friday</text><text x="180" y="139">Saturday</text><text x="210" y="139">Sunday</text>
    </g>
  </svg>
</div>

<!-- Bar attendance -->
<div class="abs crowd-card">
  <svg width="354" height="260" viewBox="0 0 202 148" font-family="Source Sans 3, sans-serif">
    <text x="101" y="16" text-anchor="middle" font-size="8" fill="#fff">BAR ATTENDANCE</text>
    <g stroke="#3bbad8" stroke-width="0.5">
      <line x1="8" y1="28" x2="196" y2="28"/><line x1="8" y1="40" x2="196" y2="40"/><line x1="8" y1="52" x2="196" y2="52"/>
      <line x1="8" y1="64" x2="196" y2="64"/><line x1="8" y1="76" x2="196" y2="76"/><line x1="8" y1="88" x2="196" y2="88"/>
      <line x1="8" y1="100" x2="196" y2="100"/><line x1="8" y1="112" x2="196" y2="112"/><line x1="8" y1="124" x2="196" y2="124"/>
      <line x1="25" y1="24" x2="25" y2="128"/><line x1="50" y1="24" x2="50" y2="128"/><line x1="73" y1="24" x2="73" y2="128"/>
      <line x1="100" y1="24" x2="100" y2="128"/><line x1="125" y1="24" x2="125" y2="128"/><line x1="150" y1="24" x2="150" y2="128"/>
      <line x1="176" y1="24" x2="176" y2="128"/>
    </g>
    <g font-size="5" fill="#8fd8ea">
      <text x="10" y="52">30 K</text><text x="10" y="76">20 K</text><text x="10" y="100">10 K</text>
    </g>
    <circle cx="100" cy="72" r="11" fill="#fff" opacity="0.3"/>
    <polyline points="25,124 50,113 73,116 100,72 125,57 150,50 176,63" fill="none" stroke="#cdeef7" stroke-width="1.4"/>
    <g fill="#fff">
      <circle cx="25" cy="124" r="2"/><circle cx="50" cy="113" r="2"/><circle cx="73" cy="116" r="2"/>
      <circle cx="100" cy="72" r="2.4"/><circle cx="125" cy="57" r="2"/><circle cx="150" cy="50" r="2"/><circle cx="176" cy="63" r="2"/>
    </g>
    <g font-size="5" fill="#8fd8ea" text-anchor="middle">
      <text x="50" y="136">JAN</text><text x="73" y="136">FEB</text><text x="100" y="136">MAR</text>
      <text x="125" y="136">APR</text><text x="150" y="136">MAY</text><text x="176" y="136">JUN</text>
    </g>
  </svg>
</div>

<!-- Other info -->
<h2 class="abs section-title">OTHER INFO :</h2>
<div class="abs section-rule"></div>

<div class="abs info-title" style="left:186px;top:1873px">POLICE RAIDS</div>
<svg class="abs" style="left:163px;top:1934px" width="180" height="180" viewBox="-50 -50 100 100" font-family="Source Sans 3, sans-serif">
  <circle r="42.5" fill="none" stroke="var(--mint)" stroke-width="11" stroke-dasharray="240 27" transform="rotate(-54)"/>
  <circle r="37" fill="var(--mint-deep)"/>
  <text y="3" text-anchor="middle" font-size="19" fill="#fff">10%</text>
  <text y="15" text-anchor="middle" font-size="7" fill="#d6f2ec">Raids</text>
</svg>

<div class="abs info-divider"></div>

<div class="abs info-title" style="left:722px;top:1875px;font-size:23px">DRINK SPECIALS</div>
<div class="abs select" style="left:722px;top:1919px">Details
  <svg class="select-caret" width="12" height="24" viewBox="0 0 12 24"><path d="M2 9l4-5 4 5zM2 15l4 5 4-5z" fill="#bbb"/></svg>
</div>
<div class="abs info-title" style="left:722px;top:1984px;font-size:23px">SPEACIAL NIGHTS</div>
<div class="abs select" style="left:722px;top:2028px">Details
  <svg class="select-caret" width="12" height="24" viewBox="0 0 12 24"><path d="M2 9l4-5 4 5zM2 15l4 5 4-5z" fill="#bbb"/></svg>
</div>

<footer class="abs footer"><span>Fim-Bosk</span> - Copyright 2013 | All rights reserved.</footer>

</body>
</html>
```